Flyer, Anzeige & Aufkleber für Massagen gestalten
Zielgruppe
Massage. Gaymassage. Wellness. Kosmetik
Aufgabenstellung
Anfertigung eines Flyers, Anzeige und Aufkleber ....

```html
<!DOCTYPE html>
<html lang="de">
<head>
<meta charset="utf-8">
<title>Massage for Men by Man</title>
<link href="https://fonts.googleapis.com/css2?family=Fira+Sans:wght@500;600&display=swap" rel="stylesheet">
<style>
  :root {
    --orange: #f26a10;
    --dark: #333333;
    --badge: #3a3a3a;
    --white: #ffffff;
    --wall-dark: #6e4632;
    --wall: #9a6a50;
    --wall-light: #b98a6e;
    --skin: #d7a488;
    --towel: #f1ebe6;
  }
  html, body { margin: 0; padding: 0; overflow: hidden; }
  body { width: 800px; height: 1200px; font-family: "Fira Sans", sans-serif; }
  .flyer { position: relative; width: 800px; height: 1200px; background: var(--dark); overflow: hidden; }
  .hero-photo {
    position: absolute; left: 0; top: 0; width: 800px; height: 798px;
    background:
      radial-gradient(ellipse 420px 180px at 260px 740px, var(--towel) 0%, rgba(241,235,230,0) 100%),
      radial-gradient(ellipse 520px 260px at 520px 640px, var(--skin) 0%, rgba(215,164,136,0) 100%),
      radial-gradient(ellipse 90px 90px at 30px 370px, rgba(255,214,150,.75) 0%, rgba(255,214,150,0) 100%),
      radial-gradient(ellipse 380px 300px at 400px 220px, var(--wall-light) 0%, rgba(185,138,110,0) 100%),
      linear-gradient(180deg, var(--wall) 0%, var(--wall-dark) 55%, var(--skin) 100%);
  }
  .accent-band { position: absolute; left: 0; top: 797px; width: 800px; height: 15px; background: var(--orange); }
  .headline { position: absolute; left: 0; top: 30px; width: 800px; text-align: center; color: var(--white); text-shadow: 0 2px 6px rgba(0,0,0,.4); }
  .headline-main { font-weight: 600; font-size: 100px; line-height: 1; letter-spacing: 1px; margin: 0; }
  .headline-rule { width: 436px; height: 3px; background: var(--white); margin: 2px auto 12px; box-shadow: 0 1px 4px rgba(0,0,0,.3); }
  .headline-sub { font-weight: 600; font-size: 56px; line-height: 1; margin: 0; letter-spacing: 0.5px; }
  .open-badge { position: absolute; left: 535px; top: 658px; width: 214px; height: 214px; }
  .services { position: absolute; left: 0; top: 864px; width: 800px; text-align: center; color: var(--white); font-weight: 600; font-size: 46px; line-height: 61px; text-shadow: 0 2px 4px rgba(0,0,0,.4); }
  .contact-line { position: absolute; left: 0; top: 1002px; width: 800px; text-align: center; color: var(--orange); font-weight: 600; font-size: 55px; line-height: 1; text-shadow: 0 2px 4px rgba(0,0,0,.4); }
  .email { position: absolute; left: 0; top: 1072px; width: 800px; text-align: center; color: var(--white); font-weight: 600; font-size: 50px; line-height: 1; text-shadow: 0 2px 4px rgba(0,0,0,.4); }
  .address { position: absolute; left: 0; top: 1139px; width: 800px; text-align: center; color: var(--orange); font-weight: 500; font-size: 23px; line-height: 1; }
</style>
</head>
<body>
<div class="flyer">
  <div class="hero-photo" role="img" aria-label="Foto: Mann entspannt auf einer Massageliege mit heißen Steinen auf dem Rücken, Kerzen und Pflanze im Hintergrund"></div>
  <div class="accent-band"></div>

  <header class="headline">
    <h1 class="headline-main">MASSAGE</h1>
    <div class="headline-rule"></div>
    <p class="headline-sub">FOR MEN BY MAN</p>
  </header>

  <svg class="open-badge" viewBox="0 0 214 214" aria-label="Kein Ruhetag – Open daily">
    <circle cx="107" cy="107" r="102" fill="var(--badge)" stroke="var(--orange)" stroke-width="9"/>
    <g transform="rotate(-15 107 107)" fill="var(--orange)" font-family="Fira Sans, sans-serif" font-weight="600" text-anchor="middle">
      <text x="107" y="100" font-size="25">Kein Ruhetag</text>
      <line x1="40" y1="110" x2="174" y2="110" stroke="var(--orange)" stroke-width="2"/>
      <text x="107" y="139" font-size="28">OPEN DAILY</text>
    </g>
  </svg>

  <div class="services">
    Seifenschaum ● Glanzkörper<br>
    Intimrasur ● Po Relax ● Tantra
  </div>
  <div class="contact-line">Klingel Tarnel | 0175/408 19 63</div>
  <div class="email">info@velorinpoint.com</div>
  <div class="address">Wiesgrund 14 | München 80331 &nbsp;| www.velorinpoint.com</div>
</div>
</body>
</html>
```